Influencer Marketing Präsentation
Zielgruppe
Ich: Influencer
Anlass: Weiterbildungs-Tagung
Zielgruppe: Teilnehmer der Digital Marketing-Weiterbildung, welche zeitgleich auch Marketing-Leute sind von Unternehmen, die etwas über Influencer Marketing erfahren möchten.
Aufgabenstellung
Ich benötige eine pfannenfertige PPTX Präsentation für meinen Vortrag an einer Digital-Marketing Tagung!
Die Präsentation ist 20min maximal, plus 10min Q&A. Sie soll cool daherkommen, aber nicht zu verspielt. Die Leute sollen sich auch denken 'wow, der hat nicht nur was als Influencer auf dem Kasten, sondern hat auch eine coole PPT zu seinem Vortrag!' Da den ganzen Tag lang unterschiedliche Leute präsentieren zu verschiedensten Marketing Themen, will ich die Präsentation locker und cool gestalten und nicht zu heftig mit Zahlen und schwerem Inhalt.
Die angehängte PPT ist ein Mix aus zwei 'alten' Präsentationen, welche ich zu dem Thema gemacht habe. Nun gilt es, die coolsten Themen rauszupicken, diese bei Bedarf auf Deutsch zu übersetzen, und allenfalls noch andere Influencer-Marketing Themen, Tips & tricks einzubauen.
Im ersten Slide der angehängten Präsentation siehst Du ein Inhaltsverzeichnis. so stelle ich mir das in etwa vor. bin aber auch offen, das ganze zu straffen!
Hier noch ein Link zu einer online verfügbaren Präsentation, von welcher ich folgende Slides integrieren möchte (anders darstellen und Umtexten bitte, damit man nicht 1:1 kopiert!) https://folienkiste.example/slide/48213907/
Slides: 5, 6, 7, 8, 11. Können auch zusammengefasst werden auf 2-3 slides!
Das fertige Projekt (Präsentation) sollte im PPTX Format angeliefert werden, so dass ich allenfalls noch letzte inhaltliche Korrekturen anbringen kann.

```html
<!DOCTYPE html>
<html lang="de">
<head>
<meta charset="utf-8">
<title>Herausforderungen – Influencer Marketing</title>
<link rel="stylesheet" href="https://fonts.googleapis.com/css2?family=Anton&family=Bodoni+Moda:wght@500;600&display=swap">
<style>
  :root {
    --slide-bg: #ffffff;
    --band-goal: #c0504d;
    --band-control: #000000;
    --band-cost: #923a38;
    --badge-red: #b01c24;
    --arc-rose: #e2b4b2;
    --tick-grey: #b9b9b9;
    --text-light: #ffffff;
  }
  html, body {
    margin: 0;
    padding: 0;
    width: 1200px;
    height: 674px;
    overflow: hidden;
    background: var(--slide-bg);
  }
  .slide {
    position: relative;
    width: 1200px;
    height: 674px;
    background: var(--slide-bg);
    overflow: hidden;
  }
  .hero-photo {
    position: absolute;
    left: 0;
    top: 0;
    width: 540px;
    height: 674px;
    background: linear-gradient(180deg, #3c4a3a 0%, #56613f 25%, #7b6a55 45%, #b9b2ad 60%, #e9ecf1 75%, #f4f5f8 100%);
  }
  .section-title {
    position: absolute;
    left: 0;
    top: 674px;
    width: 674px;
    height: 76px;
    transform: rotate(-90deg);
    transform-origin: 0 0;
    margin: 0;
    font-family: "Anton", sans-serif;
    font-weight: 400;
    font-size: 82px;
    line-height: 76px;
    letter-spacing: -1px;
    color: var(--text-light);
    white-space: nowrap;
    text-align: left;
  }
  .decor {
    position: absolute;
    left: 0;
    top: 0;
  }
  .challenge-text {
    position: absolute;
    margin: 0;
    font-family: "Bodoni Moda", serif;
    font-weight: 600;
    color: var(--text-light);
    white-space: nowrap;
    line-height: 1;
  }
  .challenge-text--goal {
    left: 482px;
    top: 140px;
    font-size: 38px;
    line-height: 47px;
  }
  .challenge-text--control {
    left: 522px;
    top: 304px;
    font-size: 76px;
    letter-spacing: 1px;
  }
  .challenge-text--cost {
    left: 482px;
    top: 461px;
    font-size: 60px;
    letter-spacing: 1px;
  }
</style>
</head>
<body>
<main class="slide">
  <div class="hero-photo" role="img" aria-label="Foto: winkender Mann in schwarzer Skijacke steht im Schnee, davor ein Kind auf einem roten Schlitten, im Hintergrund verschneiter Nadelwald"></div>

  <svg class="decor" width="1200" height="674" viewBox="0 0 1200 674" aria-hidden="true">
    <!-- rose arc -->
    <ellipse cx="189" cy="336" rx="242" ry="335" fill="none" stroke="var(--arc-rose)" stroke-width="3"/>

    <!-- bands -->
    <polygon class="band band--goal" points="431,130 1079,130 1029,231 431,231" fill="var(--band-goal)"/>
    <polygon class="band band--control" points="478,288 1079,288 1029,387 478,387" fill="var(--band-control)"/>
    <polygon class="band band--cost" points="446,448 1075,448 1025,545 446,545" fill="var(--band-cost)"/>

    <!-- badge: goal (bow & arrow) -->
    <circle cx="398" cy="176" r="66" fill="#ffffff"/>
    <g fill="none" stroke="var(--band-goal)" stroke-width="3" stroke-linecap="round" stroke-linejoin="round">
      <path d="M371 132 Q410 150 428 190 Q405 208 392 232"/>
      <path d="M371 132 L362 150 L392 232"/>
      <path d="M385 170 L440 190"/>
      <path d="M432 183 L442 190 L431 196"/>
    </g>

    <!-- badge: control (tick) -->
    <circle cx="435" cy="335" r="66" fill="#ffffff"/>
    <circle cx="435" cy="337" r="50" fill="var(--badge-red)"/>
    <path d="M405 338 L427 370 L486 300" fill="none" stroke="var(--tick-grey)" stroke-width="10" stroke-linecap="round" stroke-linejoin="round"/>

    <!-- badge: cost (dollar) -->
    <circle cx="398" cy="497" r="66" fill="#ffffff"/>
    <circle cx="398" cy="497" r="42" fill="var(--badge-red)"/>
    <text x="398" y="515" text-anchor="middle" font-family="Bodoni Moda, serif" font-weight="600" font-size="50" fill="#ffffff">$</text>
  </svg>

  <h1 class="section-title">HERAUSFORDERUNGEN</h1>

  <p class="challenge-text challenge-text--goal">GENAUE<br>ZIELSETZUNG</p>
  <p class="challenge-text challenge-text--control">KONTROLLE</p>
  <p class="challenge-text challenge-text--cost">HOHE KOSTEN</p>
</main>
</body>
</html>
```